OKAV Dispatch (e-update) Design

Using Constant Contact, we need a template news email designed that we can re-use on a regular basis. Our news email would feature an average of 10 content blocks and would love the chance to feature photos with at least 8 of the content blocks. Whatever is designed would need to be transferrable to our constant contact account. Our news content per news item is short, usually a paragraph with links back to our site and events. The template would need a banner that really showcases the email design or helps brand the email. We are looking for a design that is sophisticated but youthful. We recently rebranded our firm and are great with the use of our new corporate colors.

Target Market(s)

Our association members of 700 professional real estate managers of highrises and buildings.

Colors

Designer to choose colors to be used in the design.

Requirements
Must have
• Email template design in Constant Contact to include a banner, area for 8 to 10 content blocks with cooresponding photos. A sophisticated and colorful design that makes people want to read the content.
Should not have
• Clip art

```html
<!DOCTYPE html>
<html lang="en">
<head>
<meta charset="utf-8">
<title>OKAV Dispatch</title>
<link rel="stylesheet" href="https://fonts.googleapis.com/css2?family=Montserrat:wght@300;400;500;600&family=Open+Sans:wght@600;700&display=swap">
<style>
  :root {
    --frame: #000000;
    --white: #ffffff;
    --navy: #3d4f7c;
    --band-navy: #3f5078;
    --gold: #ffcf2a;
    --footer-gold: #deaf06;
    --panel: #f2f2f2;
    --ink: #333333;
    --muted: #9a9a9a;
    --nav: #444444;
  }
  * { box-sizing: border-box; margin: 0; padding: 0; }
  html, body { width: 1200px; height: 3093px; overflow: hidden; background: var(--frame); }
  body { font-family: "Montserrat", Arial, sans-serif; position: relative; }

  .email {
    position: absolute; left: 27px; top: 27px; width: 1144px; height: 3041px;
    background: var(--white);
  }

  /* Header */
  .header { position: relative; height: 146px; background: var(--white); }
  .brand { position: absolute; left: 163px; top: 50px; display: flex; align-items: center; gap: 14px; }
  .brand-mark { width: 38px; height: 38px; background: var(--navy); }
  .brand-name { font-weight: 600; font-size: 40px; color: var(--navy); letter-spacing: 2px; line-height: 1; }
  .nav { position: absolute; left: 548px; top: 66px; display: flex; gap: 46px; }
  .nav a { font-size: 14px; color: var(--nav); text-decoration: none; letter-spacing: 0.5px; }

  /* Hero */
  .hero-photo {
    height: 435px;
    background: linear-gradient(180deg, #1e2630 0%, #2c343b 45%, #3a4230 78%, #3f5a25 100%);
  }

  .intro { height: 361px; text-align: center; padding-top: 38px; }
  .intro-title { font-family: "Open Sans", Arial, sans-serif; font-weight: 700; font-size: 40px; color: var(--navy); letter-spacing: 0.5px; }
  .intro-text { width: 730px; margin: 30px auto 0; font-size: 16.5px; font-weight: 300; line-height: 31px; color: var(--muted); }

  .button {
    display: inline-block; background: var(--gold); color: var(--white);
    font-weight: 600; font-size: 16px; text-decoration: none; text-align: center;
    width: 156px; height: 44px; line-height: 44px;
  }
  .intro .button { margin-top: 24px; }

  /* Stories */
  .stories { position: relative; height: 1621px; background: var(--panel); }
  .story { position: absolute; left: 0; width: 1144px; height: 326px; }
  .story-photo {
    position: absolute; top: 0; width: 427px; height: 326px;
    background: linear-gradient(180deg, #5aa6df 0%, #7ab8e4 35%, #6b6458 60%, #8a7a66 80%, #8a9a4c 100%);
  }
  .story-body { position: absolute; width: 360px; }
  .story-headline { font-weight: 500; font-size: 23px; letter-spacing: 3px; color: var(--ink); }
  .story-text { margin-top: 30px; font-size: 16px; font-weight: 300; line-height: 28px; color: var(--muted); }
  .story .button { margin-top: 30px; }

  .story--photo-left .story-photo { left: 119px; }
  .story--photo-left .story-body { top: 56px; }
  .story--photo-right .story-photo { left: 608px; }
  .story--photo-right .story-body { top: 64px; text-align: right; }

  .story-1 { top: 62px; }   .story-1 .story-body { left: 585px; }
  .story-2 { top: 435px; }  .story-2 .story-body { left: 197px; }
  .story-3 { top: 825px; }  .story-3 .story-body { left: 596px; }
  .story-4 { top: 1198px; } .story-4 .story-body { left: 182px; }

  /* Tagline band */
  .tagline { height: 167px; background: var(--band-navy); text-align: center; padding-top: 48px; }
  .tagline-text { font-family: "Open Sans", Arial, sans-serif; font-weight: 700; font-size: 33px; line-height: 41px; color: var(--white); }

  /* Footer */
  .footer { height: 311px; background: var(--footer-gold); text-align: center; padding-top: 61px; color: var(--white); }
  .social { display: flex; justify-content: center; gap: 22px; }
  .social-dot { width: 46px; height: 46px; border-radius: 50%; background: var(--white); display: block; }
  .footer-text { margin-top: 30px; font-size: 19px; font-weight: 600; line-height: 29px; }
  .footer-links { margin-top: 33px; font-size: 20px; font-weight: 600; }
  .footer-links a { color: var(--white); text-decoration: none; }
  .footer-links .divider { margin: 0 8px; }
</style>
</head>
<body>
  <div class="email">
    <header class="header">
      <div class="brand">
        <span class="brand-mark"></span>
        <span class="brand-name">OKAV</span>
      </div>
      <nav class="nav">
        <a href="#">WHAT WE DO</a>
        <a href="#">INSIGHT</a>
        <a href="#">NEWS</a>
        <a href="#">ABOUT</a>
      </nav>
    </header>

    <div class="hero-photo" role="img" aria-label="Large two-storey family house with a lawn at dusk"></div>

    <section class="intro">
      <h1 class="intro-title">PROJECT TITLE HERE</h1>
      <p class="intro-text">Lorem ipsum dolor sit amet, consectetur adipiscing elit. Donec elementum enim aliquam arcu elementum hendrerit. Etiam tincidunt urna felis, non posuere eros molestie in. Sed in nisi fringilla, dapibus neque nec, sagittis ante. Etiam quis turpis sodales, cursus eros in, malesuada urna.</p>
      <a class="button" href="#">Read more</a>
    </section>

    <section class="stories">
      <article class="story story--photo-left story-1">
        <div class="story-photo" role="img" aria-label="Stone and brick suburban house under a blue sky"></div>
        <div class="story-body">
          <h2 class="story-headline">HEADLINE 1 GOES HERE</h2>
          <p class="story-text">Lorem ipsum dolor sit amet, consectetur adipiscing elit. Donec elementum enim aliquam arcu elementum hendrerit...</p>
          <a class="button" href="#">Watch video</a>
        </div>
      </article>

      <article class="story story--photo-right story-2">
        <div class="story-photo" role="img" aria-label="Stone and brick suburban house under a blue sky"></div>
        <div class="story-body">
          <h2 class="story-headline">HEADLINE 2 GOES HERE</h2>
          <p class="story-text">Lorem ipsum dolor sit amet, consectetur adipiscing elit. Donec elementum enim aliquam arcu elementum hendrerit...</p>
          <a class="button" href="#">Read more</a>
        </div>
      </article>

      <article class="story story--photo-left story-3">
        <div class="story-photo" role="img" aria-label="Stone and brick suburban house under a blue sky"></div>
        <div class="story-body">
          <h2 class="story-headline">HEADLINE 1 GOES HERE</h2>
          <p class="story-text">Lorem ipsum dolor sit amet, consectetur adipiscing elit. Donec elementum enim aliquam arcu elementum hendrerit...</p>
          <a class="button" href="#">Watch video</a>
        </div>
      </article>

      <article class="story story--photo-right story-4">
        <div class="story-photo" role="img" aria-label="Stone and brick suburban house under a blue sky"></div>
        <div class="story-body">
          <h2 class="story-headline">HEADLINE 2 GOES HERE</h2>
          <p class="story-text">Lorem ipsum dolor sit amet, consectetur adipiscing elit. Donec elementum enim aliquam arcu elementum hendrerit...</p>
          <a class="button" href="#">Read more</a>
        </div>
      </article>
    </section>

    <section class="tagline">
      <p class="tagline-text">GOOD PRICE, BETTER LIVING<br>FOR EVERYONE</p>
    </section>

    <footer class="footer">
      <div class="social">
        <a class="social-dot" href="#" aria-label="Social link 1"></a>
        <a class="social-dot" href="#" aria-label="Social link 2"></a>
        <a class="social-dot" href="#" aria-label="Social link 3"></a>
        <a class="social-dot" href="#" aria-label="Social link 4"></a>
      </div>
      <p class="footer-text">Lorem ipsum dolor sit amet, consectetuer adipiscing elit, sed diam nonummy.<br>Lorem ipsum dolor sit amet, consectetuer.</p>
      <p class="footer-links">
        <a href="#">Unsubscribe</a><span class="divider">|</span><a href="#">Manage Subscriptions</a><span class="divider">|</span><a href="#">Privacy Policy</a>
      </p>
    </footer>
  </div>
</body>
</html>
```